Birch Flooring Supply

Basic one-sided business card design using the attached logo. Vintage americana theme. Font is modified Arial Nova Cond, but anything that coordinates can be used

```html
<!DOCTYPE html>
<html lang="en">
<head>
<meta charset="utf-8">
<title>Birch Flooring Supply – Business Card</title>
<link rel="stylesheet" href="https://fonts.googleapis.com/css2?family=Barlow+Condensed:wght@600&family=Barlow:wght@400;500&display=swap">
<style>
  :root {
    --backdrop: #08090b;
    --kraft: #b9977a;
    --kraft-dark: #a9876b;
    --ink: #141210;
  }
  * { box-sizing: border-box; margin: 0; padding: 0; }
  html, body {
    width: 1200px; height: 1200px; overflow: hidden;
    background: var(--backdrop);
  }
  .canvas {
    position: relative; width: 1200px; height: 1200px;
    display: flex; align-items: center; justify-content: center;
  }
  .card {
    position: relative; width: 1050px; height: 600px;
    background: radial-gradient(ellipse at 70% 30%, var(--kraft) 0%, var(--kraft) 55%, var(--kraft-dark) 100%);
    color: var(--ink);
    font-family: "Barlow", sans-serif;
  }
  .brand {
    position: absolute; left: 62px; top: 238px;
    width: 380px;
    display: flex; align-items: center; gap: 22px;
  }
  .brand-mark {
    flex: 0 0 auto;
    width: 84px; height: 84px; border-radius: 50%;
    background: var(--ink);
  }
  .brand-name {
    font-family: "Barlow Condensed", sans-serif; font-weight: 600;
    font-size: 46px; line-height: 1.02; letter-spacing: 0.5px;
    text-transform: uppercase; color: var(--ink);
  }
  .person-name {
    position: absolute; left: 513px; top: 62px;
    font-family: "Barlow Condensed", sans-serif; font-weight: 600;
    font-size: 92px; line-height: 1; letter-spacing: -1px;
  }
  .person-role {
    position: absolute; left: 516px; top: 172px;
    font-size: 33px; letter-spacing: 2px; font-weight: 400;
  }
  .contact-table {
    position: absolute; left: 511px; top: 228px; width: 481px;
    border-collapse: collapse;
    border-top: 2px solid var(--ink); border-bottom: 2px solid var(--ink);
  }
  .contact-table td {
    border: 1.5px solid var(--ink);
    vertical-align: middle;
  }
  .contact-table tr:first-child td { border-top: none; }
  .contact-table tr:last-child td { border-bottom: none; }
  .icon-cell { width: 72px; text-align: center; }
  .icon-cell svg { width: 26px; height: 26px; display: inline-block; vertical-align: middle; }
  .value-cell {
    padding-left: 20px;
    font-variant: small-caps; letter-spacing: 2px;
    font-size: 26px;
    white-space: nowrap;
  }
  .row-phone td { height: 84px; }
  .row-phone .value-cell { font-size: 36px; font-variant: normal; letter-spacing: 3px; }
  .row-email td, .row-web td { height: 75px; }
  .row-address td { height: 82px; }
  .row-address .value-cell { font-size: 25px; line-height: 1.1; }
</style>
</head>
<body>
<main class="canvas">
  <section class="card">
    <div class="brand">
      <span class="brand-mark"></span>
      <span class="brand-name">Birch Flooring<br>Supply</span>
    </div>

    <h1 class="person-name">Daniel Reyes</h1>
    <p class="person-role">OWNER</p>

    <table class="contact-table">
      <tr class="row-phone">
        <td class="icon-cell">
          <svg viewBox="0 0 24 24" aria-hidden="true"><path fill="#141210" d="M6.6 2.5l3 3.2-1.8 2.6c1.2 2.8 3.3 5 6 6.3l2.6-1.8 3.2 3-1.7 3.5C11 18.6 5.4 13 4.4 4.3z"/></svg>
        </td>
        <td class="value-cell">555-3030-478</td>
      </tr>
      <tr class="row-email">
        <td class="icon-cell">
          <svg viewBox="0 0 24 24" aria-hidden="true"><g fill="none" stroke="#141210" stroke-width="2"><rect x="3" y="6" width="18" height="12"/><path d="M3 6l9 7 9-7M3 18l7-6M21 18l-7-6"/></g></svg>
        </td>
        <td class="value-cell">dreyes@birchfloors.com</td>
      </tr>
      <tr class="row-web">
        <td class="icon-cell">
          <svg viewBox="0 0 24 24" aria-hidden="true"><g fill="none" stroke="#141210" stroke-width="1.8"><circle cx="12" cy="12" r="9"/><ellipse cx="12" cy="12" rx="4" ry="9"/><path d="M3 12h18M5 7h14M5 17h14"/></g></svg>
        </td>
        <td class="value-cell">BIRCHFLOORS.COM</td>
      </tr>
      <tr class="row-address">
        <td class="icon-cell">
          <svg viewBox="0 0 24 24" aria-hidden="true"><path fill="#141210" d="M12 2a7 7 0 0 0-7 7c0 5 7 13 7 13s7-8 7-13a7 7 0 0 0-7-7zm0 9.5A2.5 2.5 0 1 1 12 6.5a2.5 2.5 0 0 1 0 5z"/></svg>
        </td>
        <td class="value-cell">NY Cedar Mill Road,<br>Bay 4, Unit 12/8B</td>
      </tr>
    </table>
  </section>
</main>
</body>
</html>
```